Outlast the Coming Storm - book cover

A book cover (front) to be used on print book. Book will be 5 inches by 8 inches. Also need the cover image (as jpg) for promotional purposes. Include company logo on cover - I've included a couple of versions. Include my name as author: Dr. Corliss Vandemeer

Title of book is:
Weathering Every Market Tide
(sub-title) through coaching clear reasoning

this can be a sub-sub title, or a call out or "burst" standing alone -
A survival guide for 21st century business

If you'd like some inspiration, check out my web page: www.mentorvale.com
The company colors are red, white and blue, but I think red might be too harsh - use with caution if you use it.
RGB values of the company are:
Blue: 0/66/105
Red: 190/30/45

Target Market(s)

Business / Professionals / Chief Executives of Companies with more than 1000 employees

Industry/Entity Type

Business

Font styles to use
Serif

Colors
0255a3
ffffff

Requirements
Must have
• The title should make them pause and say "I need to get this book if I want my company to survive another 20 years!"
Nice to have
• Some image that signifies the future and / or uncertainty. Should be abstract - not people, not technology (which could change and then make the book look old). If you'd like to make the design a wrap from front to back, that is fine. I am not sure what text will go on the back at this point, so I may have to come back to you in a few months for an update.

```html
<!DOCTYPE html>
<html lang="en">
<head>
<meta charset="utf-8">
<title>Weathering Every Market Tide — Book Cover</title>
<link rel="stylesheet" href="https://fonts.googleapis.com/css2?family=Old+Standard+TT:wght@400;700&family=Open+Sans:wght@700&display=swap">
<style>
  :root {
    --cover-blue: #0255a3;
    --paper: #ffffff;
    --shadow: rgba(0, 20, 60, 0.45);
  }
  html, body {
    margin: 0;
    padding: 0;
    width: 1200px;
    height: 1200px;
    overflow: hidden;
    background: var(--paper);
  }
  .canvas {
    position: relative;
    width: 1200px;
    height: 1200px;
  }
  .cover {
    position: absolute;
    left: 159px;
    top: 325px;
    width: 883px;
    height: 552px;
    background: var(--cover-blue);
    overflow: hidden;
  }
  .title {
    position: absolute;
    left: 465px;
    top: 20px;
    width: 396px;
    height: 80px;
    margin: 0;
    display: block;
  }
  .title text {
    font-family: "Old Standard TT", "Times New Roman", serif;
    font-weight: 700;
    fill: var(--paper);
  }
  .label {
    position: absolute;
    right: 22px;
    background: var(--paper);
    color: var(--cover-blue);
    font-family: "Open Sans", Arial, sans-serif;
    font-weight: 700;
    line-height: 24px;
    padding: 0 6px;
    box-shadow: 4px 4px 5px var(--shadow);
    white-space: nowrap;
  }
  .subtitle {
    top: 104px;
    font-size: 15px;
  }
  .author {
    top: 495px;
    font-size: 18px;
  }
  .artwork {
    position: absolute;
    left: 443px;
    top: 160px;
    width: 440px;
    height: 205px;
    background: linear-gradient(160deg, #ffffff 0%, #c9d9ee 30%, #0255a3 55%, #e8eef7 78%, #0255a3 100%);
  }
  .tagline {
    position: absolute;
    left: 465px;
    top: 395px;
    width: 396px;
    height: 40px;
    margin: 0;
  }
  .tagline text {
    font-family: "Old Standard TT", "Times New Roman", serif;
    font-weight: 400;
    fill: var(--paper);
  }
  .tagline line {
    stroke: var(--paper);
    stroke-width: 1.5;
  }
  .imprint {
    position: absolute;
    left: 468px;
    top: 482px;
    width: 122px;
    height: 53px;
    background: var(--paper);
    box-shadow: 4px 4px 5px var(--shadow);
    display: flex;
    align-items: center;
    justify-content: center;
    color: var(--cover-blue);
    font-family: "Open Sans", Arial, sans-serif;
    font-weight: 700;
    font-size: 19px;
  }
</style>
</head>
<body>
<main class="canvas">
  <section class="cover">
    <svg class="title" viewBox="0 0 396 80" aria-label="Weathering Every Market Tide">
      <text x="198" y="35" text-anchor="middle" font-size="31" textLength="150" lengthAdjust="spacingAndGlyphs">WEATHERING</text>
      <text x="198" y="75" text-anchor="middle" font-size="31" textLength="396" lengthAdjust="spacingAndGlyphs">EVERY MARKET TIDE</text>
    </svg>
    <div class="label subtitle">through coaching clear reasoning</div>

    <div class="artwork" role="img" aria-label="Abstract blue and white angular shards with floating question marks suggesting an uncertain future"></div>

    <svg class="tagline" viewBox="0 0 396 40" aria-label="A survival guide for 21st century business">
      <text x="0" y="27" font-size="27" textLength="396" lengthAdjust="spacingAndGlyphs">A SURVIVAL GUIDE FOR 21ST CENTURY BUSINESS</text>
      <line x1="0" y1="33" x2="396" y2="33"/>
    </svg>

    <div class="imprint">Mentorvale</div>
    <div class="label author">By : Dr. Corliss Vandemeer</div>
  </section>
</main>
</body>
</html>
```